Veltrona Cabinets Letter Head and Email Signature

Hi
I would love a design package for a letterhead, email signature, even update my business card if you like if you can come up with a great idea for my new high end cabinet shop. Veltrona Cabinets brings timeless craftsmanship to modern interiors, specializing in high end, custom cabinetry designed for architects and interior designers.

Target Market(s)

high end, luxury market

Industry/Entity Type

cabinet making

Requirements
Must have
• my colours of logo as the theme

```html
<!DOCTYPE html>
<html lang="en">
<head>
<meta charset="utf-8">
<title>Veltrona Cabinets – Stationery</title>
<link rel="stylesheet" href="https://fonts.googleapis.com/css2?family=Poppins:wght@400;500;600;700&family=Montserrat:wght@400;500;600;700&display=swap">
<style>
  :root {
    --green: #4a7c4b;
    --black: #0e0e0e;
    --grey: #e8e8e8;
    --paper: #ffffff;
    --stage: #cbcbcb;
    --ink: #1d1d1d;
    --label: #222222;
    --pattern: #eeeeee;
  }
  html, body { margin: 0; padding: 0; overflow: hidden; }
  body { width: 1200px; height: 2962px; background: var(--stage); }
  .sheet-stage { position: relative; width: 1200px; height: 2962px; overflow: hidden; background: var(--stage); font-family: "Montserrat", sans-serif; color: var(--ink); }

  .piece { position: absolute; background: var(--paper); overflow: hidden; box-shadow: 0 14px 18px rgba(0,0,0,0.22); }
  .piece-art { position: absolute; left: 0; top: 0; }
  .piece > *:not(.piece-art) { position: absolute; margin: 0; }

  .section-title { position: absolute; left: 0; width: 1200px; text-align: center; margin: 0; font-family: "Poppins", sans-serif; font-weight: 700; font-size: 60px; color: var(--label); line-height: 1; }

  .brand-mark { display: flex; align-items: center; gap: 14px; }
  .brand-mark .brand-dot { border: 3px solid var(--black); border-radius: 50%; box-sizing: border-box; flex: none; }
  .brand-name { font-family: "Poppins", sans-serif; font-weight: 400; color: var(--green); line-height: 1.02; white-space: nowrap; }

  .contact-list { list-style: none; padding: 0; }
  .contact-item { display: flex; align-items: center; white-space: nowrap; font-family: "Montserrat", sans-serif; color: var(--ink); }
  .contact-item svg { flex: none; }

  /* Letterhead */
  .letterhead { left: 233px; top: 135px; width: 735px; height: 949px; }
  .letterhead .brand-mark { left: 48px; top: 44px; }
  .letterhead .brand-dot { width: 58px; height: 58px; }
  .letterhead .brand-name { font-size: 28px; }
  .sender-name { left: 47px; top: 221px; font-family: "Poppins", sans-serif; font-weight: 600; font-size: 22px; }
  .sender-details { left: 48px; top: 258px; font-size: 12.5px; line-height: 1.35; }
  .sender-details dt { color: var(--green); font-weight: 700; display: inline; }
  .sender-details dd { display: inline; margin: 0; }
  .sender-details .detail-row { margin-bottom: 6px; }
  .sender-details .indent { padding-left: 20px; display: block; }
  .issue-date { right: 48px; top: 316px; font-size: 13px; }
  .issue-date strong { color: var(--green); font-weight: 700; }
  .letter-body { left: 49px; top: 370px; width: 640px; font-size: 10.8px; line-height: 13.4px; }
  .letter-body .salutation { font-family: "Poppins", sans-serif; font-size: 17px; font-weight: 500; margin: 0 0 8px; line-height: 1.2; }
  .letter-body p { margin: 0 0 13px; }
  .sign-off { left: 48px; top: 708px; }
  .sign-off .closing { font-size: 12px; font-weight: 700; margin: 0 0 8px; }
  .sign-off .signer { font-family: "Poppins", sans-serif; font-size: 19px; font-weight: 500; margin: 0; line-height: 1.2; }
  .sign-off .role { font-size: 12px; font-weight: 600; margin: 2px 0 0; }
  .letterhead .footer-contacts { left: 49px; top: 887px; display: flex; gap: 0; }
  .letterhead .footer-contacts .contact-item { font-size: 15px; gap: 6px; }
  .letterhead .footer-contacts .contact-item:nth-child(1) { width: 148px; }
  .letterhead .footer-contacts .contact-item:nth-child(2) { width: 281px; }

  /* Business cards */
  .card { left: 233px; width: 735px; height: 420px; }
  .card-front { top: 1300px; }
  .card-back { top: 1783px; }
  .card-front .brand-mark { left: 70px; top: 138px; gap: 26px; }
  .card-front .brand-dot { width: 116px; height: 116px; border-width: 4px; }
  .card-front .brand-name { font-size: 46px; }
  .card-handle { left: 62px; top: 309px; font-size: 27px; letter-spacing: 3px; font-weight: 500; color: var(--ink); }
  .card-back .brand-mark { left: 62px; top: 48px; gap: 18px; }
  .card-back .brand-dot { width: 72px; height: 72px; }
  .card-back .brand-name { font-size: 33px; }
  .card-name { left: 58px; top: 158px; font-family: "Montserrat", sans-serif; font-weight: 700; font-size: 40px; color: var(--green); line-height: 1.2; }
  .card-role { left: 60px; top: 207px; font-size: 23px; font-weight: 500; }
  .card-back .contact-list { left: 60px; top: 271px; }
  .card-back .contact-item { font-size: 21px; gap: 9px; height: 32px; }

  /* Email signature */
  .signature { left: 168px; top: 2433px; width: 864px; height: 287px; }
  .signature .brand-mark { left: 60px; top: 156px; gap: 20px; }
  .signature .brand-dot { width: 76px; height: 76px; }
  .signature .brand-name { font-size: 30px; }
  .sig-name { left: 384px; top: 40px; font-family: "Montserrat", sans-serif; font-weight: 700; font-size: 31px; color: var(--green); line-height: 1.2; }
  .sig-role { left: 385px; top: 80px; font-size: 18px; letter-spacing: 2px; font-weight: 500; }
  .signature .contact-list { left: 392px; top: 153px; }
  .signature .contact-item { font-size: 19px; gap: 8px; height: 30.5px; }
</style>
</head>
<body>
<main class="sheet-stage">

  <!-- LETTERHEAD -->
  <article class="piece letterhead">
    <svg class="piece-art" width="735" height="949" viewBox="0 0 735 949">
      <defs>
        <linearGradient id="lh-pattern" x1="0" y1="0" x2="1" y2="1">
          <stop offset="0" stop-color="#f4f4f4"/>
          <stop offset="1" stop-color="#ffffff"/>
        </linearGradient>
      </defs>
      <rect x="440" y="0" width="295" height="230" fill="url(#lh-pattern)" role="img" aria-label="Faint hexagon pattern"/>
      <rect x="0" y="715" width="260" height="147" fill="url(#lh-pattern)" role="img" aria-label="Faint hexagon pattern"/>
      <polygon points="0,0 439,0 346,150 0,150" fill="var(--grey)"/>
      <polyline points="238,153 356,153 419,49" fill="none" stroke="var(--black)" stroke-width="10"/>
      <polygon points="421,63 735,63 735,106 395,106" fill="var(--green)"/>
      <polygon points="0,862 712,862 668,935 0,935" fill="var(--grey)"/>
      <rect x="0" y="935" width="735" height="14" fill="var(--black)"/>
      <polygon points="690,903 735,903 735,949 662,949" fill="var(--black)"/>
      <polyline points="549,938 662,938 716,852" fill="none" stroke="var(--green)" stroke-width="7"/>
    </svg>

    <div class="brand-mark"><span class="brand-dot"></span><span class="brand-name">Veltrona<br>Cabinets</span></div>

    <h1 class="sender-name">Marcus Hollen</h1>
    <dl class="sender-details">
      <div class="detail-row"><dt>P : </dt><dd>0412558193</dd></div>
      <div class="detail-row"><dt>A : </dt><dd>Elm Street ,lane no.214<span class="indent">Harbour Road - BX2217</span></dd></div>
      <div class="detail-row"><dt>W : </dt><dd>www.veltrona.com</dd></div>
    </dl>
    <p class="issue-date"><strong>Issuing Date:</strong> May 5, 2018</p>

    <div class="letter-body">
      <p class="salutation">Dear Contributor,</p>
      <p>Thank you for your continued support of our workshop over the past season. Your feedback on finishes, hardware and joinery has shaped every piece we have delivered, and we are proud of the kitchens, libraries and dressing rooms that came to life this year. We are now preparing our next collection of bespoke cabinetry, built from carefully selected timbers and finished by hand in our studio. Each design begins with the needs of the architect and the room, and every line is drawn to suit the way the space will be lived in for many years to come.</p>
      <p>Our team works closely with interior designers from the first sketch to the final fitting, so that every drawer, door and panel sits exactly where it should. We measure twice, cut once and check every joint before it leaves the bench, keeping the quality our clients expect. Details matter to us, from the grain of the veneer to the feel of the handle and the quiet close of each door.</p>
      <p>We invite you to visit the showroom and see the new samples in person, along with the latest range of stone and brass finishes prepared for this season.</p>
      <p>Should you have a project in mind, please reach out to our studio and we will arrange a time to review your plans together. We can prepare drawings, material boards and a clear schedule, and our craftsmen will guide you through every stage of the build. Thank you again for trusting us with your spaces, and we look forward to creating something lasting with you in the months ahead, from the first meeting through to the final handover on site.</p>
    </div>

    <div class="sign-off">
      <p class="closing">Yours Sincerely</p>
      <p class="signer">Marcus Hollen</p>
      <p class="role">Director Craftsman</p>
    </div>

    <ul class="contact-list footer-contacts">
      <li class="contact-item"><svg width="16" height="16" viewBox="0 0 16 16"><circle cx="8" cy="8" r="8" fill="var(--green)"/><path d="M5 4.3l1.7-.4.9 2-1 .8a5 5 0 0 0 2.5 2.5l.8-1 2 .9-.4 1.7C8 11 4.8 7.9 5 4.3z" fill="#fff"/></svg>0412558193</li>
      <li class="contact-item"><svg width="16" height="16" viewBox="0 0 16 16"><circle cx="8" cy="8" r="8" fill="var(--green)"/><rect x="4.3" y="5.3" width="7.4" height="5.4" fill="#fff"/><polyline points="4.3,5.5 8,8.4 11.7,5.5" fill="none" stroke="var(--green)" stroke-width="0.9"/></svg>info@veltronacabinets.com.au</li>
      <li class="contact-item"><svg width="16" height="16" viewBox="0 0 16 16"><circle cx="8" cy="8" r="8" fill="var(--green)"/></svg>@veltrona.cabinets</li>
    </ul>
  </article>
  <h2 class="section-title" style="top:1146px">Letterhead</h2>

  <!-- BUSINESS CARD FRONT -->
  <article class="piece card card-front">
    <svg class="piece-art" width="735" height="420" viewBox="0 0 735 420">
      <defs>
        <linearGradient id="card-pattern" x1="0" y1="0" x2="1" y2="0">
          <stop offset="0" stop-color="#ffffff"/>
          <stop offset="0.45" stop-color="var(--pattern)"/>
          <stop offset="1" stop-color="var(--pattern)"/>
        </linearGradient>
      </defs>
      <rect x="220" y="36" width="515" height="349" fill="url(#card-pattern)" role="img" aria-label="Faint hexagon pattern"/>
      <polygon points="0,0 356,0 336,36 0,36" fill="var(--grey)"/>
      <polyline points="90,42 328,42 356,-4" fill="none" stroke="var(--black)" stroke-width="15"/>
      <polygon points="352,17 735,17 735,35 341,35" fill="var(--green)"/>
      <rect x="0" y="385" width="735" height="35" fill="var(--black)"/>
      <polygon points="640,309 735,309 735,420 575,420" fill="var(--black)"/>
      <polyline points="334,392 577,392 684,215" fill="none" stroke="var(--green)" stroke-width="13"/>
    </svg>
    <div class="brand-mark"><span class="brand-dot"></span><span class="brand-name">Veltrona<br>Cabinets</span></div>
    <p class="card-handle">@veltrona.cabinets</p>
  </article>

  <!-- BUSINESS CARD BACK -->
  <article class="piece card card-back">
    <svg class="piece-art" width="735" height="420" viewBox="0 0 735 420">
      <defs>
        <linearGradient id="card-pattern-b" x1="0" y1="0" x2="1" y2="0">
          <stop offset="0" stop-color="#ffffff"/>
          <stop offset="0.5" stop-color="var(--pattern)"/>
          <stop offset="1" stop-color="var(--pattern)"/>
        </linearGradient>
      </defs>
      <rect x="0" y="0" width="735" height="249" fill="url(#card-pattern-b)" role="img" aria-label="Faint hexagon pattern"/>
      <rect x="0" y="249" width="735" height="138" fill="var(--grey)"/>
      <rect x="0" y="387" width="735" height="33" fill="var(--black)"/>
      <polygon points="640,309 735,309 735,420 575,420" fill="var(--black)"/>
      <polyline points="334,393 577,393 684,215" fill="none" stroke="var(--green)" stroke-width="13"/>
    </svg>
    <div class="brand-mark"><span class="brand-dot"></span><span class="brand-name">Veltrona<br>Cabinets</span></div>
    <h3 class="card-name">Marcus Hollen</h3>
    <p class="card-role">Director Craftsman</p>
    <ul class="contact-list">
      <li class="contact-item"><svg width="18" height="18" viewBox="0 0 16 16"><circle cx="8" cy="8" r="8" fill="var(--green)"/><path d="M5 4.3l1.7-.4.9 2-1 .8a5 5 0 0 0 2.5 2.5l.8-1 2 .9-.4 1.7C8 11 4.8 7.9 5 4.3z" fill="#fff"/></svg>0412558193</li>
      <li class="contact-item"><svg width="18" height="18" viewBox="0 0 16 16"><circle cx="8" cy="8" r="8" fill="var(--green)"/><rect x="4.3" y="5.3" width="7.4" height="5.4" fill="#fff"/><polyline points="4.3,5.5 8,8.4 11.7,5.5" fill="none" stroke="var(--green)" stroke-width="0.9"/></svg>info@veltronacabinets.com.au</li>
      <li class="contact-item"><svg width="18" height="18" viewBox="0 0 16 16"><circle cx="8" cy="8" r="8" fill="var(--green)"/></svg>@veltrona.cabinets</li>
    </ul>
  </article>
  <h2 class="section-title" style="top:2270px">Business Card</h2>

  <!-- EMAIL SIGNATURE -->
  <article class="piece signature">
    <svg class="piece-art" width="864" height="287" viewBox="0 0 864 287">
      <defs>
        <linearGradient id="sig-pattern" x1="0" y1="0" x2="1" y2="0">
          <stop offset="0" stop-color="#ffffff"/>
          <stop offset="1" stop-color="var(--pattern)"/>
        </linearGradient>
      </defs>
      <rect x="560" y="16" width="304" height="110" fill="url(#sig-pattern)" role="img" aria-label="Faint hexagon pattern"/>
      <polygon points="0,0 304,0 263,69 0,69" fill="var(--grey)"/>
      <polyline points="75,74 259,74 304,-4" fill="none" stroke="var(--black)" stroke-width="15"/>
      <polygon points="307,0 864,0 864,16 298,16" fill="var(--green)"/>
      <rect x="0" y="126" width="864" height="145" fill="var(--grey)"/>
      <rect x="0" y="271" width="864" height="16" fill="var(--black)"/>
      <polygon points="810,235 864,235 864,287 740,287" fill="var(--black)"/>
      <polyline points="577,259 759,259 842,129" fill="none" stroke="var(--green)" stroke-width="11"/>
    </svg>
    <h3 class="sig-name">Marcus Hollen</h3>
    <p class="sig-role">Director Craftsman</p>
    <div class="brand-mark"><span class="brand-dot"></span><span class="brand-name">Veltrona<br>Cabinets</span></div>
    <ul class="contact-list">
      <li class="contact-item"><svg width="16" height="16" viewBox="0 0 16 16"><circle cx="8" cy="8" r="8" fill="var(--green)"/><path d="M5 4.3l1.7-.4.9 2-1 .8a5 5 0 0 0 2.5 2.5l.8-1 2 .9-.4 1.7C8 11 4.8 7.9 5 4.3z" fill="#fff"/></svg>0412558193</li>
      <li class="contact-item"><svg width="16" height="16" viewBox="0 0 16 16"><circle cx="8" cy="8" r="8" fill="var(--green)"/><rect x="4.3" y="5.3" width="7.4" height="5.4" fill="#fff"/><polyline points="4.3,5.5 8,8.4 11.7,5.5" fill="none" stroke="var(--green)" stroke-width="0.9"/></svg>info@veltronacabinets.com.au</li>
      <li class="contact-item"><svg width="16" height="16" viewBox="0 0 16 16"><circle cx="8" cy="8" r="8" fill="var(--green)"/></svg>@veltrona.cabinets</li>
    </ul>
  </article>
  <h2 class="section-title" style="top:2782px">Email Signature</h2>

</main>
</body>
</html>
```